IT Professional business card with a hometown feel and a little edgy.

My business name is Tamble Website Solutions. But I have ended up doing much more. I live in a very small remote community, where everyone knows everyone. We like the one-on-one customer service in this community. I do computer tutoring, virus removal, networking, and software training. My clients are businesses and private individuals.

My website is tamblewebsitesolutions.example, when I first designed it I was going for a fresh, clean look, which I still like. But I am thinking about making the website a bit more edgy to match my new logo from ArtHively (logo attached). At this time my website does not display the new logo, but I plan on redesigning the website in the future to match the logo and business card.

My tag line is "let the internet work for you"

I'm thinking I would like to have the business card printed with a metallic finish.
Updates

Please do not use black backgrounds, or any solid dark colors. Prefer light or white backgrounds.

Target Market(s)

Small businesses. Individuals that need computer help at home.

Industry/Entity Type

It Company

Contact Information for Business Card

Nora Prandell
Tamble Website Solutions
PO Box 7153
Alderport, WA 98390
Cell: 555-271-3096
nora@tamblewebsitesolutions.example
tamblewebsitesolutions.example

Font styles to use
Serif

Requirements
Must have
• Must have all the information listed in "Business Card Details"
• Must use the logo provided.
• Use the colors from the provided logo
Nice to have
• Would like to use my tagline "let the internet work for you" all lowercase

```html
<!DOCTYPE html>
<html lang="en">
<head>
<meta charset="utf-8">
<title>Tamble Website Solutions — Business Card</title>
<link rel="stylesheet" href="https://fonts.googleapis.com/css2?family=Montserrat:wght@700&family=Questrial&display=swap">
<style>
  :root {
    --green: #245f31;
    --green-light: #6db844;
    --green-mid: #3f8a3a;
    --ink: #4a4a4a;
    --paper: #ffffff;
    --backdrop: #e8ebeb;
  }
  * { margin: 0; padding: 0; box-sizing: border-box; }
  html, body {
    width: 1200px; height: 1200px; overflow: hidden;
    background: var(--backdrop);
    font-family: "Questrial", "Century Gothic", sans-serif;
  }
  .card {
    position: absolute; left: 150px;
    width: 900px; height: 514px;
    overflow: hidden;
    box-shadow: 0 6px 18px rgba(0,0,0,.12);
  }
  .card--front { top: 66px; background: var(--paper); }
  .card--back {
    top: 620px;
    background: radial-gradient(circle at 42% 48%, var(--green-light) 0%, var(--green-mid) 22%, var(--green) 52%, var(--green) 100%);
  }

  /* front */
  .corner-tab { position: absolute; left: 700px; top: 0; width: 100px; height: 80px; background: var(--green); }
  .name-band {
    position: absolute; left: 0; top: 140px; width: 340px; height: 120px;
    background: var(--green); color: var(--paper);
    padding: 14px 0 0 34px;
  }
  .person-name { font-family: "Montserrat", sans-serif; font-weight: 700; font-size: 31px; letter-spacing: .5px; line-height: 1.1; }
  .person-company { font-size: 16px; letter-spacing: 1.6px; margin-top: 6px; }
  .tagline { font-size: 18px; margin-top: 4px; }

  .brand { position: absolute; display: flex; align-items: center; }
  .brand--front { left: 370px; top: 110px; color: var(--ink); }
  .brand-square { width: 70px; height: 70px; border: 6px solid currentColor; }
  .brand--front .brand-square { border-color: var(--green); }
  .brand-divider { width: 2px; height: 110px; background: currentColor; margin: 0 26px; opacity: .7; }
  .brand-name { font-size: 30px; line-height: 1.05; }

  .contacts { position: absolute; left: 50px; top: 300px; color: var(--ink); font-size: 25px; }
  .contact-row { display: flex; align-items: center; gap: 14px; margin-bottom: 20px; }
  .contact-row svg { flex: none; }
  .address-band {
    position: absolute; left: 0; top: 420px; width: 720px; height: 52px;
    background: var(--green); color: var(--paper);
    font-size: 25px; display: flex; align-items: center; padding-left: 60px;
  }

  /* back */
  .brand--back { left: 260px; top: 170px; color: var(--paper); }
  .brand--back .brand-name { font-size: 40px; }
  .brand--back .brand-square { width: 110px; height: 110px; border-width: 8px; }
  .brand--back .brand-divider { height: 150px; }
  .back-web { position: absolute; left: 0; right: 0; top: 400px; text-align: center; color: var(--paper); font-size: 24px; }
</style>
</head>
<body>

<section class="card card--front" aria-label="Business card front">
  <div class="corner-tab"></div>

  <div class="brand brand--front">
    <div class="brand-square"></div>
    <div class="brand-divider"></div>
    <div class="brand-name">Tamble<br>Website<br>Solutions</div>
  </div>

  <div class="name-band">
    <div class="person-name">NORA PRANDELL</div>
    <div class="person-company">TAMBLE WEBSITE SOLUTIONS</div>
    <div class="tagline">let the internet work for you</div>
  </div>

  <div class="contacts">
    <div class="contact-row">
      <svg width="30" height="22" viewBox="0 0 30 22" fill="none" stroke="#245f31" stroke-width="2.5"><rect x="1.5" y="1.5" width="27" height="19"/><path d="M1.5 1.5 15 12 28.5 1.5"/></svg>
      <span>nora@tamblewebsitesolutions.example</span>
    </div>
    <div class="contact-row">
      <svg width="22" height="30" viewBox="0 0 22 30" fill="none" stroke="#245f31" stroke-width="2.5"><rect x="2" y="1.5" width="18" height="27" rx="2"/><path d="M8 24h6"/></svg>
      <span>555-271-3096</span>
      <svg width="28" height="28" viewBox="0 0 28 28" fill="none" stroke="#245f31" stroke-width="2.5" style="margin-left:14px"><circle cx="14" cy="14" r="12"/><ellipse cx="14" cy="14" rx="5" ry="12"/><path d="M2 14h24M4 8h20M4 20h20"/></svg>
      <span>tamblewebsitesolutions.example</span>
    </div>
  </div>

  <div class="address-band">PO Box 7153 Alderport, WA 98390</div>
</section>

<section class="card card--back" aria-label="Business card back">
  <div class="brand brand--back">
    <div class="brand-square"></div>
    <div class="brand-divider"></div>
    <div class="brand-name">Tamble<br>Website<br>Solutions</div>
  </div>
  <div class="back-web">tamblewebsitesolutions.example</div>
</section>

</body>
</html>
```